WP website design (FELM)

We need a wordpress design that will incorporate a professional color scheme with company logo in a clean layout. The design needs to consider that this will be developed on a responsive theme. Colors are undetermined - those that will complement the logo.
Client mentions liking brintonsale.example for the layout and use of color. Possible but not necessary to have large slideshow element.

Industry/Entity Type

It Company

Font styles to use
Sans Serif

Colors

Designer to choose colors to be used in the design.

Requirements
Must have
• - Navigation: 1)Home 2) Auctions 3) Services 4) About Us 5) FAQs 6) References 7) Contact Us

Site will have slideshow, please use high-end stock real estate image initially. Header will have logo. Social icons (Social link one, Social link two, Social link three)

Widgets Include: Email signup form, Featured Auctions, Featured Video widget.

Footer will have contact info (below), site navigation, smaller company logo, affiliation logos (attached).

FELM Auction Group
4172 Quill Ferry Lane
Linden Hollow, TN 38917
1-800-555-BIDS (2437)
Ph. (615) 555-0148
Fx. (615) 555-0193
Nice to have
• - Site will have drop-down menus - please indicate the styling, for instance the dropdown menus 1) Live 2) Online 3) Past - under the 'Auctions' link

```html
<!DOCTYPE html>
<html lang="en">
<head>
<meta charset="utf-8">
<title>FELM Auction Group</title>
<link rel="stylesheet" href="https://fonts.googleapis.com/css2?family=Oswald:wght@300;400;500;600&family=Arimo:wght@400;700&display=swap">
<style>
:root{
  --brown:#6b3a16;
  --red:#d9141b;
  --panel:#f1f1f1;
  --rule:#d6d6d6;
  --text:#222;
  --footer:#e9e9e9;
}
*{box-sizing:border-box;margin:0;padding:0}
html,body{width:922px;height:1200px;overflow:hidden;background:#fff}
body{position:relative;font-family:'Arimo',Arial,sans-serif;color:var(--text)}
a{color:inherit;text-decoration:none}

.brand{position:absolute;left:88px;top:30px;display:flex;align-items:center;gap:8px}
.brand-dot{width:26px;height:26px;border-radius:50%;background:var(--brown)}
.brand-name{font-family:'Oswald',sans-serif;font-weight:600;font-size:24px;line-height:1;color:var(--red);width:110px}

.social{position:absolute;top:17px;left:719px;display:flex;gap:12px}
.social span{width:33px;height:33px;border-radius:50%;background:var(--brown);display:block}

.main-nav{position:absolute;top:59px;left:332px;display:flex;align-items:center;font-family:'Oswald',sans-serif;font-size:16px;color:var(--brown)}
.main-nav a{padding:4px 16px}
.main-nav a.current{border:1px solid var(--red);color:var(--red);border-radius:2px;padding:5px 17px}

.hero{position:absolute;left:59px;top:126px;width:803px;height:240px;background:linear-gradient(180deg,#3f6a2a 0%,#8a5a38 35%,#a97a55 65%,#5b4030 100%)}
.hero-caption{position:absolute;left:101px;top:44px;width:259px;height:96px;background:rgba(255,255,255,.6);text-align:center;font-family:'Oswald',sans-serif;color:#111}
.hero-caption .big{font-size:36px;font-weight:400;line-height:1;margin-top:14px}
.hero-caption .small{font-size:19px;font-weight:300;margin-top:4px}
.hero-arrow{position:absolute;top:105px;width:27px;height:30px;background:#fff;display:flex;align-items:center;justify-content:center}
.hero-arrow.prev{left:0}.hero-arrow.next{right:0}

.section-title{position:absolute;display:flex;align-items:center;font-family:'Oswald',sans-serif;font-weight:300;font-size:19px;color:#222;white-space:nowrap}
.section-title::after{content:"";flex:1;height:1px;background:var(--rule);margin-left:6px}

.auction{position:absolute;left:68px;width:522px;background:var(--panel);border-radius:4px}
.auction .photo{position:absolute;left:17px;top:12px;width:170px;height:94px;border:3px solid #fff;box-shadow:0 0 0 1px #ddd}
.auction .details{position:absolute;left:58px;width:88px;height:24px;background:var(--brown);color:#fff;font-family:'Oswald',sans-serif;font-size:15px;text-align:center;line-height:24px}
.auction .body{position:absolute;left:198px;width:320px;font-size:10.4px;line-height:17.6px}
.bid-btn{display:inline-block;background:var(--red);color:#fff;font-family:'Oswald',sans-serif;font-size:15px;padding:0 11px;height:24px;line-height:24px;margin:7px 0 6px 6px}
.meta{margin-left:8px;font-size:10.4px;line-height:17.6px}
.meta .type{color:var(--brown);font-weight:700}
.meta b{font-weight:700}

.newsletter{position:absolute;left:606px;top:382px;width:240px;height:188px;background:var(--brown);border-radius:4px;text-align:center;color:#fff}
.newsletter h3{font-family:'Oswald',sans-serif;font-weight:300;font-size:19px;margin-top:10px}
.newsletter p{font-size:11px;margin-top:2px}
.newsletter .field{margin:6px auto 0;width:216px;height:24px;background:#fff;color:#222;font-size:10px;text-align:left;padding-left:7px;line-height:24px}
.newsletter .create{margin:8px auto 0;width:88px;height:24px;background:var(--red);font-family:'Oswald',sans-serif;font-size:16px;line-height:24px}

.featured{position:absolute;left:606px;top:618px;width:240px;height:200px;background:var(--panel);border-radius:4px;padding:6px 6px 0}
.feat-item{display:flex;gap:8px;height:64px;border-bottom:1px dotted #bbb;padding-top:2px}
.feat-item+.feat-item{padding-top:6px}
.feat-thumb{width:73px;height:48px;flex:none}
.feat-text{font-size:9.8px;line-height:12px;padding-top:3px}
.feat-links{margin-top:6px;display:flex;gap:22px;font-weight:700;color:var(--brown);text-decoration:underline}

.video{position:absolute;left:606px;top:874px;width:240px;height:136px;background:var(--panel);border-radius:4px}
.video .frame{position:absolute;left:8px;top:7px;width:224px;height:120px;background:linear-gradient(180deg,#6d8f5a 0%,#c9b48a 45%,#6e9a3c 100%)}

.footer{position:absolute;left:59px;top:1036px;width:803px;height:164px;background:var(--footer);border-top:3px solid #c8c8c8}
.foot-nav{position:absolute;left:14px;top:12px;list-style:none;font-family:'Oswald',sans-serif;font-size:14px;color:#333}
.foot-nav li{height:20px;display:flex;align-items:center;gap:9px}
.foot-nav li::before{content:"";border-left:5px solid var(--red);border-top:4px solid transparent;border-bottom:4px solid transparent}
.foot-nav li.current{color:var(--red)}
.foot-contact{position:absolute;left:218px;top:14px;font-size:10.4px;line-height:22.4px}
.foot-contact h4{font-family:'Oswald',sans-serif;font-weight:400;font-size:16px;color:var(--red);line-height:20px;margin-bottom:2px}
.foot-brand{position:absolute;left:430px;top:60px;display:flex;align-items:center;gap:8px}
.foot-brand .brand-name{width:110px}
.badges{position:absolute;left:617px;top:47px;display:flex;gap:10px;align-items:center}
.badges span{display:block;background:#555;border-radius:3px}
.copyright{position:absolute;left:616px;top:116px;font-size:9.8px;line-height:18px;color:#333}
.copyright b{color:var(--red)}
</style>
</head>
<body>

<header>
  <a class="brand" href="#"><span class="brand-dot"></span><span class="brand-name">FELM Auction Group</span></a>
  <div class="social" aria-label="Social links">
    <span aria-label="Social link one"></span><span aria-label="Social link two"></span><span aria-label="Social link three"></span>
  </div>
  <nav class="main-nav">
    <a class="current" href="#">Home</a>
    <a href="#">Auctions</a>
    <a href="#">Services</a>
    <a href="#">About</a>
    <a href="#">FAQs</a>
    <a href="#">References</a>
    <a href="#">Contact</a>
  </nav>
</header>

<section class="hero" role="img" aria-label="Large brick two-storey house with garages surrounded by trees">
  <div class="hero-caption"><div class="big">100%</div><div class="small">SATISFACTION GUARANTEED</div></div>
  <span class="hero-arrow prev"><svg width="10" height="18" viewBox="0 0 10 18"><path d="M9 1L1 9l8 8" fill="none" stroke="var(--brown)" stroke-width="1.5"/></svg></span>
  <span class="hero-arrow next"><svg width="10" height="18" viewBox="0 0 10 18"><path d="M1 1l8 8-8 8" fill="none" stroke="var(--brown)" stroke-width="1.5"/></svg></span>
</section>

<h2 class="section-title" style="left:66px;top:386px;width:524px">ONLINE PERSONAL PROPERTY AUCTION</h2>
<article class="auction" style="top:414px;height:199px">
  <div class="photo" role="img" aria-label="Two-storey suburban house with garden" style="background:linear-gradient(180deg,#4d86c9 0%,#8fb7da 40%,#7a8a6a 70%,#5a7a3a 100%)"></div>
  <a class="details" href="#" style="top:122px">Details</a>
  <div class="body" style="top:14px">
    <p>Lorem Ipsum is simply dummy text of the printing and typesetting industry. Lorem Ipsum has been the industry's standard dummy text ever since the 1500s, when an unknown printer took a galley of type and scrambled it to make a type specimen book. It has survived not only five centuries, but also the leap into electronic</p>
    <a class="bid-btn" href="#">Click for Online Bidding</a>
    <div class="meta"><div class="type">Online Bidding Only</div><div><b>Began:</b> 10/03/14 at 9:00 AM EDT</div><div><b>Ends:</b> 10/09/14 at 7:00 PM EDT</div></div>
  </div>
</article>

<h2 class="section-title" style="left:69px;top:633px;width:521px">ONLINE REAL ESTATE AUCTION</h2>
<article class="auction" style="top:661px;height:159px">
  <div class="photo" role="img" aria-label="Shingled house on a green lawn" style="background:linear-gradient(180deg,#5a8fd0 0%,#9ec1e4 35%,#8a6a55 60%,#4f8a2e 100%)"></div>
  <a class="details" href="#" style="top:122px">Details</a>
  <div class="body" style="top:14px">
    <p>Lorem Ipsum is simply dummy text of the printing and typesetting industry. Lorem Ipsum has been the industry's standard dummy text ever since the 1500s, when an unknown printer took a galley of...</p>
    <a class="bid-btn" href="#" style="margin-left:2px">Click for Online Bidding</a>
    <div class="meta" style="margin-left:4px"><div class="type">Online Bidding Only</div><div><b>Began:</b> 10/03/14 at 9:00 AM EDT</div><div><b>Ends:</b> 10/09/14 at 7:00 PM EDT</div></div>
  </div>
</article>

<h2 class="section-title" style="left:70px;top:841px;width:520px">ABSOLUTE ONLINE REAL ESTATE AUCTIONN</h2>
<article class="auction" style="top:870px;height:140px">
  <div class="photo" role="img" aria-label="White house with orange tiled roof" style="background:linear-gradient(180deg,#3f7fd0 0%,#9cc3ea 40%,#c8663a 55%,#efeae0 75%,#6a8a3a 100%)"></div>
  <a class="details" href="#" style="top:111px">Details</a>
  <div class="body" style="top:14px">
    <p>Lorem Ipsum is simply dummy text of the printing and typesetting industry. Lorem Ipsum has been the industry's standard dummy text...</p>
    <a class="bid-btn" href="#">Click for Online Bidding</a>
    <div class="meta"><div class="type">Online Bidding Only</div><div><b>Began:</b> 10/03/14 at 9:00 AM EDT</div><div><b>Ends:</b> 10/09/14 at 7:00 PM EDT</div></div>
  </div>
</article>

<aside>
  <form class="newsletter">
    <h3>NEWSLETTER</h3>
    <p>Create your Account</p>
    <div class="field" style="margin-top:7px">Email</div>
    <div class="field">Username</div>
    <div class="field">Pasword</div>
    <div class="create">Create</div>
  </form>

  <h2 class="section-title" style="left:607px;top:589px;width:239px">FEATURED AUCTION</h2>
  <div class="featured">
    <div class="feat-item"><div class="feat-thumb" role="img" aria-label="Suburban house" style="background:linear-gradient(180deg,#5a8fd0,#8a8a70 60%,#5a7a3a)"></div><div class="feat-text">Lorem Ipsum is simply dummy text Lorem Ipsum is simply...<div class="feat-links"><span>Details</span><span>Photos</span></div></div></div>
    <div class="feat-item"><div class="feat-thumb" role="img" aria-label="White house with trees" style="background:linear-gradient(180deg,#6a9ad6,#dcdcdc 55%,#5a8a3a)"></div><div class="feat-text">Lorem Ipsum is simply dummy text Lorem Ipsum is simply...<div class="feat-links"><span>Details</span><span>Photos</span></div></div></div>
    <div class="feat-item"><div class="feat-thumb" role="img" aria-label="Modern house with pool" style="background:linear-gradient(180deg,#8fb3d6,#e8e8e8 50%,#2a8ad0)"></div><div class="feat-text">Lorem Ipsum is simply dummy text Lorem Ipsum is simply...<div class="feat-links"><span>Details</span><span>Photos</span></div></div></div>
  </div>

  <h2 class="section-title" style="left:607px;top:845px;width:239px">FEATURED VIDEO</h2>
  <div class="video">
    <div class="frame" role="img" aria-label="Video still of a single-storey home with garden">
      <svg style="position:absolute;left:92px;top:40px" width="40" height="40" viewBox="0 0 40 40"><circle cx="20" cy="20" r="18" fill="rgba(255,255,255,.25)" stroke="#fff" stroke-width="2"/><path d="M15 11l14 9-14 9z" fill="#fff"/></svg>
    </div>
  </div>
</aside>

<footer class="footer">
  <ul class="foot-nav">
    <li class="current">Home</li><li>Auctions</li><li>Services</li><li>About</li><li>FAQs</li><li>References</li><li>Contact</li>
  </ul>
  <div class="foot-contact">
    <h4>FELM Auction Group</h4>
    <div>4172 Quill Ferry Lane</div>
    <div>Linden Hollow, TN 38917</div>
    <div>1-800-555-BIDS (2437)</div>
    <div>Call: (615) 555-0148</div>
    <div>FAX : (615) 555-0193</div>
  </div>
  <div class="foot-brand"><span class="brand-dot"></span><span class="brand-name">FELM Auction Group</span></div>
  <div class="badges" aria-label="Affiliations">
    <span style="width:28px;height:28px"></span>
    <span style="width:56px;height:26px;border-radius:50%"></span>
    <span style="width:34px;height:28px"></span>
    <span style="width:28px;height:32px"></span>
  </div>
  <div class="copyright">Copyright © 2014 • <b>FELM Auction Group</b><br>• All Rights Reserved</div>
</footer>

</body>
</html>
```